Interfaith organization needs a poster advertising event for youth

We need a poster advertising our annual Lantern Gathering and Summit, where youth of all different religions come together for dialogue, friendship, fun, art, and musical performances. The poster should be have a front advertising the event, and the back should have more detailed descriptions of the event and submissions. It should be fun and eye catching!

Target Market(s)

Youth and Religious Organizations

Industry/Entity Type

Festival

Font styles to use
Serif

Requirements
Must have
• Pictures, poster-feel, contact information, etc. Logos of Bright Harbor Allies and Crossroads Young Leaders Circle of Maple Valley

```html
<!DOCTYPE html>
<html lang="en">
<head>
<meta charset="utf-8">
<title>Lantern Gathering and Summit – Poster</title>
<link href="https://fonts.googleapis.com/css2?family=Oswald:wght@400;500&family=Source+Sans+3:wght@400;600;700&display=swap" rel="stylesheet">
<style>
:root{
  --red:#e8352a;
  --orange:#f26a22;
  --yellow:#f7a81b;
  --ink:#3a3a3a;
  --paper:#ffffff;
  --backdrop:#e9e6e2;
  --photo-warm:#b58d6a;
  --photo-deep:#6a4c3a;
}
*{box-sizing:border-box;margin:0;padding:0}
html,body{width:1200px;height:782px;overflow:hidden}
body{background:var(--backdrop);position:relative;font-family:"Source Sans 3",sans-serif;color:var(--ink)}
.page{position:absolute;top:40px;width:527px;height:682px;background:var(--paper);overflow:hidden;box-shadow:0 3px 10px rgba(0,0,0,.25)}
.page--front{left:59px}
.page--back{left:620px}
.abs{position:absolute}
.heading{font-family:"Oswald",sans-serif;font-weight:500;text-transform:uppercase;line-height:1.15}
.photo{position:absolute;background:linear-gradient(135deg,var(--photo-warm),var(--photo-deep))}
.photo-frame{position:absolute;background:#fff;padding:6px;box-shadow:0 2px 6px rgba(0,0,0,.3)}
.photo-frame .photo{position:relative;width:100%;height:100%}
/* front */
.hero-photo{left:0;top:0;width:527px;height:245px}
.side-strip{right:0;top:296px;width:18px;height:283px;background:var(--orange)}
.title-block{left:131px;top:197px;width:170px;color:#fff;font-size:12px}
.seal{left:40px;top:172px;width:78px;height:78px;border-radius:50%;background:#fff;border:3px solid var(--yellow);display:flex;align-items:center;justify-content:center;text-align:center;font-size:8.5px;font-weight:700;color:var(--red);line-height:1.1;padding:8px}
.date-ribbon{left:120px;top:266px;width:196px;transform:rotate(5deg);color:#fff;font-size:16px;text-align:center}
.time{left:232px;top:309px;color:#fff;font-size:11px;font-family:"Oswald",sans-serif;transform:rotate(5deg)}
.highlights{left:38px;top:368px;list-style:none;font-size:17px}
.highlights li{line-height:22.5px}
.highlights .alt{color:var(--yellow)}
.highlights .main{color:var(--red)}
.venue{left:43px;top:470px;font-size:11px;line-height:18px}
.partners{left:40px;top:520px;display:flex;align-items:center;gap:14px}
.partner{display:flex;align-items:center;gap:6px;font-size:12px;font-weight:700;color:#2b3a8f;line-height:1.1}
.partner-mark{width:40px;height:40px;background:#2b3a8f;flex:none}
.partner-mark--round{border-radius:50%;width:26px;height:26px;background:none;border:2px solid #2b3a8f}
.footer{left:0;top:579px;width:527px;height:51px;display:flex}
.footer-left{width:264px;background:var(--yellow);color:#fff;font-weight:700;font-size:12px;display:flex;align-items:center;padding-left:20px}
.footer-right{flex:1;background:var(--orange);color:#fff;font-weight:700;font-size:11.5px;display:flex;align-items:center;justify-content:center}
.web{left:0;top:630px;width:527px;height:52px;display:flex;align-items:center;justify-content:center;color:var(--red);font-size:23px;letter-spacing:1px}
/* back */
.back-header{left:0;top:22px;width:527px;text-align:center;font-family:"Oswald",sans-serif;font-size:13px;color:var(--ink)}
.theme-banner{left:82px;top:60px;width:365px;height:42px;background:var(--yellow);color:#fff;font-size:19px;display:flex;align-items:center;justify-content:center;text-transform:none}
.sub-heads{left:0;top:116px;width:527px;text-align:center;color:var(--orange);font-size:16px}
.intro{left:38px;top:183px;width:451px;text-align:center;font-size:10.3px;line-height:11px}
.info-card{left:16px;top:246px;width:490px;height:330px;background:#fff;transform:rotate(-.6deg);box-shadow:0 2px 8px rgba(0,0,0,.3);padding:12px 14px;text-align:center;font-size:10.2px;line-height:11px}
.info-card h3{color:var(--orange);font-size:11px;font-weight:600;margin-top:2px}
.info-card .note{margin:7px 0 6px;font-weight:600}
</style>
</head>
<body>

<section class="page page--front">
  <div class="photo hero-photo" role="img" aria-label="Teen musicians performing tabla, vocals and sitar in front of faith banners"></div>
  <svg class="abs" style="left:0;top:0" width="527" height="682" viewBox="0 0 527 682">
    <polygon points="0,188 110,250 0,360" fill="#f7a81b"/>
    <polygon points="405,0 470,0 527,57 527,122" fill="#e8352a"/>
    <text x="0" y="0" transform="translate(436,10) rotate(45)" font-family="Oswald" font-size="13" fill="#fff">IS RELIGION COOL?</text>
    <polygon points="45,192 287,162 294,290 238,300 217,357 45,318" fill="#e8352a"/>
    <polygon points="123,256 328,276 322,318 118,296" fill="#f7a81b"/>
    <polygon points="118,296 322,318 316,332 140,316" fill="#c8281f"/>
  </svg>
  <div class="abs seal">Crossroads Young Leaders Circle</div>
  <div class="abs heading title-block">Crossroads Young Leaders Circle of Maple Valley's 13th Annual Lantern Gathering &amp; Summit</div>
  <div class="abs heading date-ribbon">Sunday March 19th, 2017</div>
  <div class="abs time">11:00AM-5:00PM</div>
  <div class="abs side-strip"></div>
  <div class="photo-frame" style="left:352px;top:246px;width:162px;height:112px;transform:rotate(5deg)"><div class="photo" role="img" aria-label="Dancer in festive costume performing"></div></div>
  <div class="photo-frame" style="left:350px;top:362px;width:166px;height:110px;transform:rotate(-4deg)"><div class="photo" role="img" aria-label="Group of young singers performing on stage"></div></div>
  <div class="photo-frame" style="left:356px;top:478px;width:164px;height:112px;transform:rotate(5deg)"><div class="photo" role="img" aria-label="Students seated in a row making heart shapes with their hands"></div></div>
  <ul class="abs heading highlights">
    <li class="main">• Teens expressing their faith through<br>&nbsp;&nbsp;art, music, and dialogue</li>
    <li class="alt">• Interfaith youth forum</li>
    <li class="main">• This year's theme <span style="text-transform:none">"Is Religion Cool?"</span></li>
  </ul>
  <div class="abs venue">Harmony Hall Community Center<br>4210 Orchard Lane, Maple Valley, CA 90410</div>
  <div class="abs partners">
    <div class="partner"><span class="partner-mark"></span>Crossroads Young<br>Leaders Circle</div>
    <div class="partner"><span class="partner-mark partner-mark--round"></span>Bright Harbor<br>Allies</div>
  </div>
  <div class="abs footer">
    <div class="footer-left">For further details, contact (555) 214-0387</div>
    <div class="footer-right">hello@crossroadsmv.org | Social: @CrossroadsMV</div>
  </div>
  <div class="abs heading web">www.crossroadsmv.org</div>
</section>

<section class="page page--back">
  <svg class="abs" style="left:0;top:0" width="527" height="682" viewBox="0 0 527 682">
    <polygon points="0,190 80,250 0,250" fill="#f7a81b"/>
    <polygon points="43,53 98,53 82,80 98,102 43,102 58,78" fill="#f26a22"/>
    <polygon points="484,53 429,53 445,80 429,102 484,102 469,78" fill="#f26a22"/>
    <rect x="498" y="296" width="29" height="283" fill="#f26a22"/>
  </svg>
  <div class="abs back-header">CROSSROADS YOUNG LEADERS CIRCLE OF MAPLE VALLEY'S 13TH ANNUAL LANTERN GATHERING &amp; SUMMIT</div>
  <div class="abs heading theme-banner">THIS YEAR'S THEME "Is Religion Cool?"</div>
  <div class="abs heading sub-heads">Teens expressing their faith through art, music, and dialogue<br>Interfaith youth forum</div>
  <p class="abs intro">All high school age faith groups are invited to come and join with 150 to 175 other high school students from various faith traditions to participate in the Crossroads Young Leaders Circle of Maple Valley's Annual Interfaith Youth Forum. More than ever, our county and world need young leaders who are willing to learn from each other and build stronger communities!</p>
  <div class="abs info-card">
    <h3>SUMMIT</h3>
    <p>The purpose of this Interfaith Youth Forum is to bring together young people from diverse ethnic, cultural, and religious backgrounds, and to engage them in dialogue. True dialogue is a conversation on a common subject between two or more persons of differing points of view and/or backgrounds. We feel that this commitment to dialogue will affect relationships in a constructive way in our places of worship and in our community.<br>The forum itself involves having eight religiously diverse high school-age students, one adult, and youth leader around each table to discuss common questions. Our youth leaders act as facilitators, but it is stressed that it is the students we want to hear from.</p>
    <p class="note">RSVP for our SUMMIT by February 19th, 2017</p>
    <h3>LANTERN GATHERING</h3>
    <p>The forum will be followed by the Lantern Gathering where families of the participants are welcomed to join. The Gathering will include musical performances of all types from diverse religious communities. The differing performing arts include but are not limited to singing, dancing, instrumental music, storytelling, etc.</p>
    <p class="note">To Participate in our Lantern Gathering (Music, Song, Dance), RSVP by February 25th, 2017</p>
    <h3>ART GALLERY</h3>
    <p>This event will include an Art Gallery display of students' work, highlighting their expressions of faith, and artwork promoting learning, understanding, leadership, and service. Art includes any painting, illustration, sculpture, photography or other visual art.</p>
    <p class="note">Art Work for our Art Gallery must be submitted by: March 10th, 2017</p>
  </div>
  <div class="abs footer">
    <div class="footer-left">For further details, contact (555) 214-0387</div>
    <div class="footer-right">hello@crossroadsmv.org | Social: @CrossroadsMV</div>
  </div>
  <div class="abs heading web">www.crossroadsmv.org</div>
</section>

</body>
</html>
```